Online travel site needs edgy website design

tripnook is the first Global Business Travel Website that provides the most comprehensive destination information tailored to suit the business traveller.

It is a ‘one click solution’ that offers direct access to all aspects of business travel, including general information on the city, accommodation and transportation options, economic and financial statistics, key business and services contacts, as well as leisure activities, entertainment suggestions, and listings for any personal needs.

Much more than a travel website, tripnook.com eliminates the need to buy multiple travel books or visit scores of websites. Most importantly, it is the only website that will cover such an extensive range of destinations around the world, while also featuring cities where information is really scarce. The user-friendly and consistent format for all destinations will allow the business traveller to easily navigate through more than 100 information pages on any destination.

tripnook will be simple to navigate, intuitive, unique in design, dynamic, and content rich providing a supreme user experience during navigation of the website.

The website will initially be English and is set to expand to more languages in the future.

A beta site with back-end database has been built - and now we need an edgy state of the art graphic design to reskin it.

LOOK & FEEL

Scope
The design of the site should reflect tripnook’s corporate and user centric philosophy with the following elements:

a. tripnook corporate image and branding
b. the promotion of each city destination
c. tripnook being the starting point of travel, while also a partner during travel
d. the subtle but powerful presence of advertising and sponsorship

All the above must derive from the design outline and elements that are going to be used.

Design Guidelines

Innovative and elegant design, minimalism, simplicity that permits the offering of the required information to be delivered in line with the values of Trust, Care, Discovery & Connection.

In addition:

1. The usability, navigation and the informative character of the corporate web site should not be compromised by the design.
2. The over-segmented pages and over-crowded content per page should be avoided.
3. The design should not only guide the user in an inviting way to the information required but also to intrigue them for further navigation.
4. Advertising space should be anticipated in line with the design character and OMR standard ad sizes.
5. The use of photos / videos should also encouraged.

Key Elements

a. Branding/Logos
Throughout the website branding should be present as a “guarantee seal” for the content accuracy. Corporate logo should be placed on every page while branding should also characterise any content element and/or tool. Appendix contains the current brand guidelines. Should additional sub-logos be required for specific sections, these should be proposed.

b. Fonts
Provided your experience on the website design you are requested to propose alternative font types and sizes always taken into consideration the inviting and user friendly character that the new website should aspire to. The font type that will be proposed must be user friendly in English typography, but also could support other languages in the future.

Given the fact that the majority of the text in the website contains information and listing, the fonts and text layout should not strain and fatigue the reader.

c. SEO
The design should be friendly towards the search engines.

d. Colours
Colour is considered as an integral part of the brand identity. Tripnook.com corporate colours are orange and grey as per the Attached document reference guide.

Different tonalities of the brand colours, or colours in general, should be proposed and applied, guided always by the above described scope of Look & Feel.

e. Section Headings
As presented above, the site’s section headings (refer Overview of the Site.) The principle is to label the content following users’ needs and mindset. However, the label space should be flexible for changes. The labels should facilitate the user to understand the content they host. This is important and should be applied especially to informative content.

Another function that Headings should perform is that of promoting the website’s content, especially when this kind of content will make the user spend more time in the website. This category of Headings should be approached in a more creative and attractive way as to intrigue users to check the content hosted.

f. Icons
Icons are considered necessary in order to provide the user extra help to guide them to reach the information they need quick n’ easy. Icons not only contribute actively to the creation of an attractive look & feel but, most importantly, facilitate navigation and speed up the users’ familiarisation with the website too.

Therefore their design should be eye-catching, comprehensive and dynamic, in accordance to the new site’s colour coding and following the latest trends as these were defined by the look & feel of smart phones.

PIXELHIVE BRIEF REQUIREMENTS
Based on the above, please provide at least two (2) approaches for the following pages – this includes colour palette in line with logo, layout, fonts.

Initial submissions can just address Deliverable 1 & 2 to fine tune design before proceeding further.

Please refer sample screenshots separately attached from raw beta site for content – available for Deliverables 2 -6.

(REFER example sites we like for their creativity: http://www.quillark-studio.co.uk/#Background, http://www.pelorafestas.com.br/, http://brambletondesign.co.uk/ )

Deliverable 1: Landing /Home page
- Access log in –
o Free Account or via WorkLattice/Chatterly etc
o Membership Access – Login
- How to use the site
- Allowance for video or animation
- Destination Selection
- Blog & Social media links

Deliverable 2: Destination Landing Page / Template
This is essentially a city guide template to be used for all cities throughout the site.

This page clearly depicts the four information sections
1. General
2. Business
3. Leisure
4. Personal

Also this page should include:
- Business News Feed
- Advertising & Sponsorship Spaces (according to OMR Standards)
- Destination Time, Weather, FX rates (LIVE feeds)
- Tips

Deliverable 3: Follow the above format but show an Internal Content Page – text only with subheadings

Deliverable 4: Follow the above format but show an Internal Content Page – text and photos

Deliverable 5: Follow the above format but show an Internal Content Page – Listing Sections such as Restaurants (this must also include filter categories)

Deliverable 6: Follow the above format but show an Internal Content Page – Top 10 Experiences – this incorporates address and contact details, photo and sub-text

Deliverable 7: The Membership Landing Page which should include:
1. Intro
2. Advertising & Sponsorship Space
3. The four sections
4. Tips Section
Updates

Hi all - just to reiterate that we are open to different approaches in the design.  We only included the existing screen shots of the beta site to provide you with an idea of the content.  We definitely don't want to see anything similar.....we want it to be edgy yet simple and easy to navigate....we want to create an outstanding user experience!  Cheers Tripnook Team

Reason: Dear Designers - We are extending the period as have not had many submissions at all and want to provide more time. If you have already submitted, we will be in touch shortly with feedback. Thanks for your understanding Tripnook Team

Reason: We would like to give everyone more time so we can find the best and most preferred design.

Target Market(s)

TARGET MARKET
tripnook is a consumer focused website, offering a wide-range of easy-to-use and interactive platforms, for informative and commercial purposes, while also providing attractive and innovative advertising real-estate for potential business partners.

The target audience can be segmented as follows:

Primary Target: Professionals travelling on Business

They require up-to-date reliable information prior and during their travel, as well as facilitation to take action. They need an online Personal Assistant.

The personal characteristics of the primary target group are: busy life, tailored solutions, reliable sources, trusting, caring, and spoiled.
 
The website will have a membership option (for a small annual fee) which will provide customized information for their demographic and preferences. Sub target groups will include:
1. Business Men 40 years
3. Business Women 40 years
5. Business People with reduced mobility

Demographic & Travelling Profile of Business Travellers

• 92% of them use the internet as a source of info
• 54% are males, 38 years old
• 80% holds a college/university degree
• 68% is travelling mainly for leisure and annually 6 times per year
• 52% reserve their ticket through the internet
• 66% is travel internationally

Secondary Targets:

Executive PA’s
Executive personal assistants who need to plan their manager’s travel and provide support information for their trip.

Professionals travelling for Leisure and Partners
They have most probably used the website for their business travel, but consider it also useful for their leisure travel. The generic website, will include enough information to cover most of the leisure needs, as well as the requirements of their partners.

Direct Business-to-Business [B2B] Targets
The direct [B2B] targeted audience includes corporations that would like to use a white label solution for their staff, by using all available destinations or a selected number depending on their global network.

Business-to-Business [B2B] Targets
The [B2B] targeted audience is an indirect audience, for which tripnook promotes its services, and a key revenue stream. The B2B audience consists mainly of a diverse range of professional organisations targeting the business traveller (airlines, hotels, travel agencies, tourism authorities, entertainment companies, services, etc.) tripnook will be targeting these organisations to advertise on the site.
 
Desired Response from Target Groups

The desired response from the consumer targets is:
a) Recurrent use of website
b) Share content/experience with friends and social networking sites
c) Interact on the website’s Blog
d) Register for newsletters and offers
e) Subscribe to Membership
f) Be exposed to commercial advertisements on the website
g) Provide feedback (in the future) for services
h) Use (in the future) online services to purchase products and services
Competition

Industry/Entity Type

Travel

Requirements
Must have
• A clean crisp and professional appearance giving a sense of Trust and Reliability.
Should not have
• It should not look like every other run of the mill travel sites - Roomvale.com, Jaunteo etc

```html
<!DOCTYPE html>
<html lang="en">
<head>
<meta charset="utf-8">
<title>tripnook – Home</title>
<link rel="stylesheet" href="https://fonts.googleapis.com/css2?family=Yanone+Kaffeesatz:wght@400;500&family=Bree+Serif&family=Signika:wght@300;400;600&family=Open+Sans:wght@400;600&display=swap">
<style>
  :root {
    --orange: #f47a1f;
    --orange-dark: #e2660c;
    --blue: #1a8cf0;
    --ink: #4a4a4a;
    --ink-soft: #6b6b6b;
    --page: #f3f3f3;
    --panel: #ffffff;
    --line: #e4e4e4;
    --footer: #555555;
  }
  * { box-sizing: border-box; margin: 0; padding: 0; }
  html, body { width: 948px; height: 1200px; overflow: hidden; }
  body {
    position: relative;
    background: var(--page);
    font-family: "Signika", sans-serif;
    font-weight: 300;
    color: var(--ink);
  }
  .top-strip { position: absolute; left: 0; top: 0; width: 948px; height: 5px; background: var(--orange); }

  /* header */
  .brand { position: absolute; left: 59px; top: 30px; display: flex; align-items: center; gap: 12px; }
  .brand-mark { width: 52px; height: 52px; background: var(--orange); border-radius: 4px; }
  .brand-name { font-family: "Signika", sans-serif; font-weight: 600; font-size: 50px; color: var(--orange); letter-spacing: -1px; line-height: 1; }
  .account-tab {
    position: absolute; left: 770px; top: 0; width: 124px; height: 37px;
    background: var(--orange); border-radius: 0 0 10px 10px;
    display: flex; align-items: center; justify-content: center; gap: 8px;
    font-family: "Open Sans", sans-serif; font-size: 12.5px; color: #fff;
  }
  .phone { position: absolute; left: 777px; top: 50px; display: flex; align-items: center; gap: 9px;
    font-family: "Open Sans", sans-serif; font-weight: 600; font-size: 14px; color: var(--orange); }
  .phone-dot { width: 18px; height: 18px; border-radius: 50%; background: #1aa6e4; }

  .main-nav {
    position: absolute; left: 0; top: 132px; width: 948px; height: 64px;
    background: #f7f7f7;
    box-shadow: inset 0 6px 8px -6px rgba(0,0,0,.18), 0 6px 8px -6px rgba(0,0,0,.18);
  }
  .main-nav a {
    position: absolute; top: 24px; font-family: "Open Sans", sans-serif; font-size: 12.5px;
    color: var(--ink); text-decoration: none; white-space: nowrap;
  }
  .main-nav a.is-current { color: var(--orange); }

  /* hero */
  .hero-title { position: absolute; left: 50px; top: 226px; font-family: "Yanone Kaffeesatz", sans-serif; font-weight: 500; font-size: 42px; color: var(--ink); white-space: nowrap; }
  .hero-text { position: absolute; left: 50px; top: 281px; width: 360px; font-size: 17.5px; line-height: 25px; color: var(--ink-soft); }
  .btn {
    position: absolute; display: flex; align-items: center; justify-content: center;
    font-family: "Bree Serif", serif; color: #fff; border-radius: 9px; text-decoration: none; white-space: nowrap;
  }
  .btn-orange { background: var(--orange); }
  .btn-blue { background: var(--blue); }
  .btn-lg { font-size: 20px; height: 46px; }
  .btn-md { font-size: 19px; height: 44px; }
  .btn-sm { font-size: 18px; height: 31px; border-radius: 8px; }
  .hero-art {
    position: absolute; left: 433px; top: 198px; width: 440px; height: 312px;
    background: radial-gradient(ellipse at 55% 55%, #f6d24a 0%, #e9443a 45%, #b8c6bd 75%, rgba(243,243,243,0) 100%);
    border-radius: 40% 30% 40% 35%;
  }

  /* panels */
  .panel { position: absolute; background: var(--panel); border: 1px solid var(--line); }
  .panel-title { font-family: "Yanone Kaffeesatz", sans-serif; font-weight: 500; color: var(--ink); white-space: nowrap; }
  .guide { left: 50px; top: 567px; width: 851px; height: 349px; }
  .guide .panel-title { position: absolute; left: 20px; top: 10px; font-size: 40px; }
  .guide-text { position: absolute; left: 21px; top: 68px; width: 278px; font-size: 13.6px; line-height: 24px; color: var(--ink-soft); }
  .guide-text p + p { margin-top: 24px; }
  .video { position: absolute; left: 325px; top: 12px; width: 515px; height: 314px; border: 1px solid #dcdcdc; background: #fff; }
  .video-frame { position: absolute; left: 0; top: 0; width: 513px; height: 288px;
    background: linear-gradient(135deg, #f2f2f2 0%, #e8dccf 40%, #5a9bd6 60%, #f6f6f6 100%); }
  .video-bar { position: absolute; left: 0; bottom: 0; width: 513px; height: 24px; background: #1b1b1b; }
  .video-progress { position: absolute; left: 0; top: 0; height: 3px; width: 513px; background: #3a3a3a; }
  .video-progress span { display: block; width: 30px; height: 3px; background: #cc1e1e; }
  .video-time { position: absolute; left: 80px; top: 6px; font-family: "Open Sans", sans-serif; font-size: 9px; color: #ddd; }

  .card { top: 934px; width: 272px; height: 158px; }
  .card .panel-title { position: absolute; left: 13px; top: 8px; font-size: 31px; }
  .select {
    position: absolute; left: 12px; top: 56px; width: 231px; height: 32px; border: 1px solid #bdbdbd; border-radius: 3px;
    font-family: "Open Sans", sans-serif; font-size: 10px; color: #777; padding: 10px 8px; background: #fff;
  }
  .select svg { position: absolute; right: 10px; top: 11px; }
  .card-text { position: absolute; left: 13px; top: 52px; width: 250px; font-size: 13.4px; line-height: 24px; color: var(--ink-soft); }
  .card-note { position: absolute; left: 28px; top: 54px; width: 230px; font-family: "Open Sans", sans-serif; font-size: 10.5px; line-height: 15px; color: #333; }
  .social { position: absolute; left: 32px; top: 91px; display: flex; gap: 8px; }
  .social span { width: 24px; height: 26px; border-radius: 4px; }

  /* footer */
  .site-footer { position: absolute; left: 0; top: 1110px; width: 948px; height: 66px; background: var(--footer);
    display: flex; align-items: center; justify-content: center; padding-top: 8px; }
  .site-footer a { font-family: "Open Sans", sans-serif; font-size: 11px; color: #fff; text-decoration: none; white-space: nowrap; }
  .site-footer .sep { color: #fff; font-size: 12px; margin: 0 18px; }
  .copyright { position: absolute; left: 0; top: 1176px; width: 948px; height: 24px; background: var(--orange);
    color: #fff; font-family: "Open Sans", sans-serif; font-size: 10px; display: flex; align-items: center; justify-content: center; }
</style>
</head>
<body>
  <div class="top-strip"></div>

  <header>
    <div class="brand"><span class="brand-mark"></span><span class="brand-name">tripnook</span></div>
    <div class="account-tab"><span>Login</span><span>|</span><span>Sign Up</span></div>
    <div class="phone"><span class="phone-dot"></span><span>123 456 7890</span></div>
  </header>

  <nav class="main-nav">
    <a class="is-current" style="left:82px">Home</a>
    <a style="left:166px">About Us</a>
    <a style="left:266px">How to Use</a>
    <a style="left:377px">Select Destination</a>
    <a style="left:526px">Register</a>
    <a style="left:622px">My Account</a>
    <a style="left:738px">Blog</a>
    <a style="left:813px">Contact Us</a>
  </nav>

  <section class="hero">
    <h1 class="hero-title">Lorem Ipsum dolor sit amet</h1>
    <p class="hero-text">Lorem ipsum dolor sit amet, consectetur adipiscing elit. Donec facilisis turpis augue, sit amet lacinia neque tempor sed.</p>
    <a class="btn btn-orange btn-lg" style="left:48px;top:371px;width:165px">Member Login</a>
    <a class="btn btn-blue btn-lg" style="left:222px;top:371px;width:180px">Chatterly Login</a>
    <div class="hero-art" role="img" aria-label="Illustration of a country map in red and yellow with a beach chair, parasol, sun, cathedral and bull"></div>
  </section>

  <section class="panel guide">
    <h2 class="panel-title">How to use the site</h2>
    <div class="guide-text">
      <p>Donec malesuada vehicula ipsum, eget dictum mauris laoreet et. Nam id est ante. Curabitur eget nibh et mi ultrices vestibulum.</p>
      <p>Morbi volutpat, felis quis iaculis vulputate, tellus sapien mattis sem, eget malesuada diam metus ut tortor. Aliquam sed cursus leo. Mauris eu eros et nibh dictum dictum nec a augue.</p>
    </div>
    <a class="btn btn-orange btn-md" style="left:22px;top:279px;width:124px">Read More</a>
    <div class="video">
      <div class="video-frame" role="img" aria-label="Video still of a traveller with a backpack reading a map"></div>
      <div class="video-bar">
        <div class="video-progress"><span></span></div>
        <svg width="60" height="24" viewBox="0 0 60 24" style="position:absolute;left:10px;top:0">
          <rect x="6" y="8" width="2.5" height="9" fill="#ccc"/><rect x="11" y="8" width="2.5" height="9" fill="#ccc"/>
          <path d="M44 11h3l4-3v10l-4-3h-3z" fill="#ccc"/>
        </svg>
        <span class="video-time">0:14 / 4:05</span>
      </div>
    </div>
  </section>

  <section class="panel card" style="left:50px">
    <h3 class="panel-title">Select Destination</h3>
    <div class="select">Select City
      <svg width="12" height="8" viewBox="0 0 12 8"><path d="M1 1l5 5 5-5" stroke="#333" stroke-width="2" fill="none"/></svg>
    </div>
    <a class="btn btn-orange btn-sm" style="left:12px;top:102px;width:106px">Submit</a>
  </section>

  <section class="panel card" style="left:339px">
    <h3 class="panel-title">Latest Blog</h3>
    <p class="card-text">Morbi volutpat, felis quis iaculis vulputate, tellus sapien mattis sem, eget malesuada</p>
    <a class="btn btn-orange btn-sm" style="left:14px;top:104px;width:130px">More Post</a>
  </section>

  <section class="panel card" style="left:629px">
    <h3 class="panel-title">Get In Touch</h3>
    <p class="card-note">Pleae clcik on the icons and get in ytouch with us and get all the updates.</p>
    <div class="social" aria-label="Social network links">
      <span style="background:#3b5b99"></span>
      <span style="background:#34b4e4"></span>
      <span style="background:#2b2b2b"></span>
      <span style="background:#0b77b5"></span>
      <span style="background:#e8e8e8"></span>
    </div>
  </section>

  <footer class="site-footer">
    <a>Home</a><span class="sep">|</span>
    <a>About Us</a><span class="sep">|</span>
    <a>FAQs</a><span class="sep">|</span>
    <a>SiteMap</a><span class="sep">|</span>
    <a>Contact Us</a><span class="sep">|</span>
    <a>Sitemap</a><span class="sep">|</span>
    <a>Privacy Policy</a><span class="sep">|</span>
    <a>Advertise</a><span class="sep">|</span>
    <a>Terms &amp; Use</a>
  </footer>
  <div class="copyright">© 2013, All Rights Reserved</div>
</body>
</html>
```